Website Redesign for Existing BBQ Catering Company

Need to get my website (HickoryHound.com) redesigned. Looking for a cleaner look but still patriotic and rustic. Would like to add parallax scrolling on the menu page and include some pics from our photo gallery. Would like to display a picture of the brisket before scrolling into the meat section of our menu and the same for the other sections too.....picture of one of our sides, appetizers, desserts, etc.

Would also like to add three new pages called Corporate Events, Weddings, and Veteran Events possibly in a drop-down menu called Catering. You can use pics from our Facebook page. We've posted tons of pics from weddings that we've done. I've uploaded some corporate and wedding pics but you can pics the ones that look best. I can swap them out later if needed.

Would like to keep it Wordpress if possible so I can update it as needed.

Also need to add some links to our storefront on The Vow Loft. I have the HTML code and will upload the image here.

Also need to add social media links for our Facebook, Instagram and Twitter pages.

The contact form that I'm using now feeds the leads into another site called Ledgerly.com that I use to manage my clients.

Target Market(s)

Weddings, corporate events, veterans

Industry/Entity Type

Catering

Coding

Coded - Design and coding required

Number of Pages Required

5+ page

Colors
ec1f27
3176b5
ffffff

Requirements
Must have
• Really like the hero image design. Looks less like a template. Check out https://maurins.com and https://fennelgrovetaos.com
• Would like to keep somewhat of a rustic and patriotic look and feel like the site currently is. We mainly cater in barn weddings and we cater for a lot of veterans. Will be pushing more corporate catering next year and opening a restaurant.

```html
<!DOCTYPE html>
<html lang="en">
<head>
<meta charset="utf-8">
<title>Hickory Hound BBQ</title>
<link href="https://fonts.googleapis.com/css2?family=Courgette&family=Cinzel:wght@700&family=Open+Sans:ital,wght@0,400;0,600;0,700;1,400;1,600&display=swap" rel="stylesheet">
<style>
:root{
  --red:#ec1f27;
  --blue:#0d4f9c;
  --blue-light:#3176b5;
  --white:#ffffff;
  --ink:#1b1b1b;
  --muted:#555555;
  --footer:#050505;
  --wood-a:#6b4a35;
  --wood-b:#8a6650;
}
*{margin:0;padding:0;box-sizing:border-box}
html,body{width:1200px;height:3863px;overflow:hidden}
body{
  position:relative;
  font-family:'Open Sans',sans-serif;color:var(--ink);
  background:linear-gradient(90deg,var(--wood-a),var(--wood-b) 30%,var(--wood-a) 55%,var(--wood-b) 80%,var(--wood-a));
}
.page{position:absolute;left:124px;top:0;width:945px;height:3745px;background:var(--white);overflow:hidden}
.abs{position:absolute}
.script{font-family:'Courgette',cursive;font-weight:400}

/* hero */
.hero{left:0;top:0;width:945px;height:597px;
  background:radial-gradient(ellipse at 40% 40%,#7a4a3a,#3b2320 60%,#1c1210);}
.topbar{top:8px;font-size:12px;font-weight:600;color:var(--white)}
.topbar svg{vertical-align:-2px;margin-right:6px}
.nav{left:0;top:67px;width:945px;height:46px;background:rgba(255,255,255,.82)}
.nav a{position:absolute;top:15px;font-size:12px;font-weight:600;color:var(--ink);text-decoration:none}
.nav a.active{border-bottom:3px solid var(--blue);padding-bottom:9px}
.brand-mark{width:176px;height:176px;border-radius:50%;background:var(--white);
  display:flex;align-items:center;justify-content:center;text-align:center;
  font-family:'Cinzel',serif;font-weight:700;font-size:21px;line-height:1.2;color:var(--red)}
.hero-welcome{left:0;width:945px;top:282px;text-align:center;font-size:50px;color:var(--white)}
.hero-rule{left:184px;width:577px;top:355px;height:1px;background:rgba(255,255,255,.7)}
.hero-title{left:0;width:945px;top:356px;text-align:center;font-family:'Cinzel',serif;font-weight:700;font-size:56px;letter-spacing:3px;color:var(--white)}
.btn-outline{border:2px solid var(--white);color:var(--white);font-size:18px;font-weight:600;display:flex;align-items:center;justify-content:center;text-transform:uppercase}

/* section titles */
.section-title{left:0;width:945px;text-align:center;font-size:36px;color:var(--ink)}
.section-title span{background:var(--white);padding:0 20px;position:relative}
.section-title::before{content:"";position:absolute;left:0;right:0;top:50%;height:2px;background:var(--ink)}
.section-title.light{color:var(--white)}
.section-title.light::before{background:var(--white)}
.section-title.light span{background:none}

/* products */
.card-photo{width:273px;height:193px}
.card-base{width:273px;height:127px;display:flex;align-items:center;justify-content:center}
.card-base .label{width:216px;height:59px;border:4px solid var(--white);display:flex;align-items:center;justify-content:center;color:var(--white);font-size:15px;font-weight:700}
.arrow{width:41px;height:62px;display:flex;align-items:center;justify-content:center}

/* feature */
.feature{left:0;top:1133px;width:945px;height:404px;background:var(--blue)}
.feature h2{position:absolute;left:41px;top:58px;font-size:27px;line-height:1.35;color:var(--white);font-style:italic}
.feature p{position:absolute;left:41px;top:185px;width:390px;font-size:17px;line-height:1.6;color:var(--white)}
.btn-red{background:var(--red);color:var(--white);font-size:17px;font-weight:600;display:flex;align-items:center;justify-content:center}

/* specialties */
.spec-grid{left:41px;top:1666px;width:875px;height:255px;display:grid;grid-template-columns:repeat(5,175px);grid-template-rows:repeat(2,127.5px);box-shadow:0 0 0 1px #ddd}
.spec-text{background:var(--white);padding:22px 12px 0;text-align:center}
.spec-text h3{font-size:12px;font-weight:700;margin-bottom:8px}
.spec-text p{font-size:10px;line-height:1.5;color:var(--muted)}

/* services */
.services{left:0;top:1962px;width:945px;height:510px;background:linear-gradient(180deg,#2a1814,#4a2a22 50%,#1e1210)}
.service{width:274px;height:276px;color:var(--white);text-align:center;padding-top:68px}
.service h3{font-size:21px;font-weight:600;margin-bottom:12px}
.service p{font-size:16px;line-height:1.55;padding:0 26px}
.service .more{display:inline-block;margin-top:22px;font-size:15px;font-weight:600;text-decoration:underline}
.service-icon{position:absolute;left:50%;top:-40px;transform:translateX(-50%)}

/* menu */
.dish{width:160px;height:160px;border-radius:50%;border:3px solid var(--white);box-shadow:0 0 0 2px #ccc}
.dish-name{font-size:22px;font-weight:600}
.dish-text{font-size:10px;line-height:1.45;color:var(--muted);width:100px}
.dish-more{font-size:11px;font-weight:700;color:var(--blue)}

/* gallery & testimonial */
.gallery-band{left:0;top:2820px;width:945px;height:420px;background:var(--blue)}
.band-title{font-size:36px;color:var(--white);font-style:italic}
.thumb{width:116px;height:85px;border:4px solid var(--white)}
.avatar{width:120px;height:120px;border-radius:50%;border:5px solid var(--white);background:linear-gradient(135deg,#c9a68c,#7a5a45)}
.quote-name{font-size:18px;font-weight:700;color:var(--white)}
.quote{font-size:15px;line-height:1.5;font-style:italic;font-weight:600;color:var(--white);width:300px}

/* flag & footer */
.flag-band{left:0;top:3239px;width:945px;height:126px;
  background:linear-gradient(90deg,#b81d24,#e8e8e8 30%,#c21f26 48%,#1f3f8a 62%,#f0f0f0 80%,#1f3f8a)}
.footer{left:0;top:3365px;width:945px;height:380px;background:var(--footer);color:var(--white)}
.footer h4{position:absolute;top:125px;font-size:13px;font-weight:400;font-style:italic;letter-spacing:.5px}
.footer p,.footer li{font-size:13px;line-height:1.65}
.footer ul{list-style:none}
.email-field{border:2px solid var(--white);font-size:11px;font-style:italic;color:#bbb;padding:12px 14px}
.copyright{font-size:13px;font-style:italic;font-weight:600}
.social{width:26px;height:26px;border-radius:50%;background:var(--blue-light)}
.footer-line{left:0;top:3739px;width:945px;height:6px;background:var(--blue)}
</style>
</head>
<body>
<main class="page">

  <!-- hero -->
  <section class="abs hero" role="img" aria-label="Close-up photo of sliced smoked brisket with a dark bark"></section>
  <div class="abs topbar" style="left:15px">
    <svg width="12" height="12" viewBox="0 0 24 24"><path fill="#fff" d="M6.6 10.8a15 15 0 0 0 6.6 6.6l2.2-2.2c.3-.3.7-.4 1-.2 1.1.4 2.3.6 3.6.6.6 0 1 .4 1 1V20c0 .6-.4 1-1 1A17 17 0 0 1 3 4c0-.6.4-1 1-1h3.5c.6 0 1 .4 1 1 0 1.3.2 2.5.6 3.6.1.3 0 .7-.2 1z"/></svg>555-014-2290
  </div>
  <div class="abs topbar" style="right:10px">
    <svg width="13" height="10" viewBox="0 0 26 20"><rect x="1" y="1" width="24" height="18" fill="none" stroke="#fff" stroke-width="2"/><path d="M1 1l12 10L25 1" fill="none" stroke="#fff" stroke-width="2"/></svg>hello@hickoryhound.com
  </div>
  <nav class="abs nav">
    <a class="active" style="left:87px">HOME</a>
    <a style="left:167px">ABOUT US</a>
    <a style="left:270px">PRODUCTS</a>
    <a style="left:592px">MENU</a>
    <a style="left:666px">BLOG POST</a>
    <a style="left:777px">CONTACT US</a>
  </nav>
  <div class="abs brand-mark" style="left:388px;top:25px">Hickory<br>Hound<br>BBQ</div>
  <div class="abs hero-welcome script" style="font-style:italic">Welcome To</div>
  <div class="abs hero-rule"></div>
  <div class="abs hero-title">HICKORY HOUND BBQ</div>
  <div class="abs btn-outline" style="left:381px;top:453px;width:188px;height:49px">Read More</div>

  <!-- products -->
  <h2 class="abs section-title script" style="top:633px"><span>Our Products</span></h2>
  <div class="abs arrow" style="left:0;top:845px;background:var(--blue)"><svg width="12" height="18" viewBox="0 0 12 18"><path d="M10 2L3 9l7 7" stroke="#fff" stroke-width="3" fill="none"/></svg></div>
  <div class="abs arrow" style="left:904px;top:845px;background:var(--red)"><svg width="12" height="18" viewBox="0 0 12 18"><path d="M2 2l7 7-7 7" stroke="#fff" stroke-width="3" fill="none"/></svg></div>

  <div class="abs card-photo" style="left:41px;top:749px;background:linear-gradient(160deg,#8c7a68,#4a3a2c)" role="img" aria-label="Catering table with a wooden platter of appetizers"></div>
  <div class="abs card-base" style="left:41px;top:942px;background:var(--red)"><div class="label">CEDAR ROW RANCH</div></div>
  <div class="abs card-photo" style="left:337px;top:749px;background:linear-gradient(160deg,#a0704c,#5a3a24)" role="img" aria-label="Buffet line of chafing dishes with barbecue sides"></div>
  <div class="abs card-base" style="left:337px;top:942px;background:var(--blue)"><div class="label">CEDAR ROW RANCH</div></div>
  <div class="abs card-photo" style="left:633px;top:749px;background:linear-gradient(160deg,#6a3a36,#c9a590)" role="img" aria-label="Tray of small dessert cups with berries"></div>
  <div class="abs card-base" style="left:633px;top:942px;background:var(--blue)"><div class="label">CEDAR ROW RANCH</div></div>

  <!-- feature -->
  <section class="abs feature">
    <h2 class="script">We mainly cater in barn weddings &amp;<br>we cater for a lot of veterans</h2>
    <p>It is a long established fact that a reader will be distracted by the readable content of a page when looking at its layout.</p>
    <div class="abs btn-red" style="left:41px;top:317px;width:198px;height:56px">LEARN MORE</div>
    <div class="abs" style="left:571px;top:39px;width:346px;height:218px;background:linear-gradient(135deg,#6a5a4a,#2a2420)" role="img" aria-label="Barn venue with catering tables set up"></div>
    <div class="abs" style="left:481px;top:116px;width:314px;height:260px;border:6px solid var(--white);background:radial-gradient(circle at 50% 45%,#3a3a3a,#141414 60%,#5a5a5a)" role="img" aria-label="Cast iron pot on a smoker"></div>
  </section>

  <!-- specialties -->
  <h2 class="abs section-title script" style="top:1576px"><span>Our Specialities</span></h2>
  <div class="abs spec-grid">
    <div class="spec-text"><h3>Cedar Row Ranch</h3><p>It is a long established fact that a reader will be distracted by the readable</p></div>
    <div style="background:linear-gradient(135deg,#b24a4a,#3a2a28)" role="img" aria-label="Glasses and drinks on a reception table"></div>
    <div class="spec-text"><h3>Cedar Row Ranch</h3><p>It is a long established fact that a reader will be distracted by the readable</p></div>
    <div style="background:linear-gradient(135deg,#c08060,#5a3020)" role="img" aria-label="Event hall with draped tables"></div>
    <div class="spec-text"><h3>Cedar Row Ranch</h3><p>It is a long established fact that a reader will be distracted by the readable</p></div>
    <div style="background:linear-gradient(135deg,#9a6a48,#4a3020)" role="img" aria-label="Pan of baked beans and sides"></div>
    <div class="spec-text"><h3>Cedar Row Ranch</h3><p>It is a long established fact that a reader will be distracted by the readable</p></div>
    <div style="background:linear-gradient(135deg,#a0402a,#3a1a14)" role="img" aria-label="Ribs and sausages on a grill"></div>
    <div class="spec-text"><h3>Cedar Row Ranch</h3><p>It is a long established fact that a reader will be distracted by the readable</p></div>
    <div style="background:linear-gradient(135deg,#b08a6a,#5a4030)" role="img" aria-label="Plated barbecue with bread rolls"></div>
  </div>

  <!-- services -->
  <section class="abs services" role="img" aria-label="Dim photo of a banquet hall set for an event"></section>
  <h2 class="abs section-title light script" style="top:1988px"><span>Our Services</span></h2>
  <div class="abs service" style="left:31px;top:2132px;background:var(--red)">
    <svg class="service-icon" width="74" height="80" viewBox="0 0 74 80"><polygon points="37,2 72,21 72,59 37,78 2,59 2,21" fill="#fff"/><circle cx="37" cy="32" r="6" fill="#ec1f27"/><circle cx="24" cy="36" r="4.5" fill="#ec1f27"/><circle cx="50" cy="36" r="4.5" fill="#ec1f27"/><path d="M28 54v-8a9 9 0 0 1 18 0v8zM17 54v-6a7 7 0 0 1 9-6v12zM57 54v-6a7 7 0 0 0-9-6v12z" fill="#ec1f27"/></svg>
    <h3>Corporate Events</h3><p>Fusce gravida, ipsum eu luctus sodales, quam libero scelerisque</p><span class="more">READ MORE</span>
  </div>
  <div class="abs service" style="left:345px;top:2132px;background:var(--blue)">
    <svg class="service-icon" width="74" height="80" viewBox="0 0 74 80"><polygon points="37,2 72,21 72,59 37,78 2,59 2,21" fill="#fff"/><circle cx="30" cy="32" r="6" fill="#0d4f9c"/><circle cx="45" cy="32" r="6" fill="#0d4f9c"/><path d="M20 56v-9a10 10 0 0 1 20 0v9zM36 56v-9a10 10 0 0 1 18 0v9z" fill="#0d4f9c"/></svg>
    <h3>Weddings</h3><p>Fusce gravida, ipsum eu luctus sodales, quam libero scelerisque</p><span class="more">READ MORE</span>
  </div>
  <div class="abs service" style="left:643px;top:2132px;background:var(--blue)">
    <svg class="service-icon" width="74" height="80" viewBox="0 0 74 80"><polygon points="37,2 72,21 72,59 37,78 2,59 2,21" fill="#fff"/><rect x="21" y="26" width="32" height="28" rx="2" fill="none" stroke="#0d4f9c" stroke-width="3"/><rect x="21" y="26" width="32" height="7" fill="#0d4f9c"/><rect x="27" y="38" width="5" height="5" fill="#0d4f9c"/><rect x="35" y="38" width="5" height="5" fill="#0d4f9c"/><rect x="43" y="38" width="5" height="5" fill="#0d4f9c"/><rect x="27" y="46" width="5" height="5" fill="#0d4f9c"/></svg>
    <h3>Veteran Events</h3><p>Fusce gravida, ipsum eu luctus sodales, quam libero scelerisque</p><span class="more">READ MORE</span>
  </div>

  <!-- menu -->
  <h2 class="abs section-title script" style="top:2510px"><span>Our Menu</span></h2>
  <div class="abs arrow" style="left:0;top:2657px;width:26px;height:42px;background:var(--red)"><svg width="10" height="14" viewBox="0 0 10 14"><path d="M8 1L2 7l6 6" stroke="#fff" stroke-width="2.5" fill="none"/></svg></div>
  <div class="abs arrow" style="left:919px;top:2657px;width:26px;height:42px;background:var(--red)"><svg width="10" height="14" viewBox="0 0 10 14"><path d="M2 1l6 6-6 6" stroke="#fff" stroke-width="2.5" fill="none"/></svg></div>

  <div class="abs dish" style="left:38px;top:2598px;background:linear-gradient(160deg,#7a3a30,#e0d0c0 50%,#3a2a40)" role="img" aria-label="Flag-themed dessert platter"></div>
  <div class="abs dish-name" style="left:211px;top:2632px">Desserts</div>
  <div class="abs dish-text" style="left:211px;top:2668px">Fresh daily, smoked low and slow, served hot.</div>
  <div class="abs dish-more" style="left:211px;top:2728px">READ MORE</div>

  <div class="abs dish" style="left:332px;top:2598px;background:linear-gradient(160deg,#6a2a20,#c0806a 55%,#3a1a14)" role="img" aria-label="Sliced brisket on a board"></div>
  <div class="abs dish-name" style="left:505px;top:2632px">Brisket</div>
  <div class="abs dish-text" style="left:505px;top:2668px">Fresh daily, smoked low and slow, served hot.</div>
  <div class="abs dish-more" style="left:505px;top:2728px">READ MORE</div>

  <div class="abs dish" style="left:625px;top:2598px;background:linear-gradient(160deg,#5a2a24,#b06048 55%,#2a1a14)" role="img" aria-label="Tray of appetizers on a buffet"></div>
  <div class="abs dish-name" style="left:789px;top:2632px">Appetizers</div>
  <div class="abs dish-text" style="left:789px;top:2668px">Fresh daily, smoked low and slow, served hot.</div>
  <div class="abs dish-more" style="left:789px;top:2728px">READ MORE</div>

  <!-- gallery & testimonial -->
  <section class="abs gallery-band"></section>
  <h2 class="abs band-title script" style="left:46px;top:2880px">Gallery</h2>
  <div class="abs thumb" style="left:46px;top:2956px;background:linear-gradient(135deg,#a06a40,#3a2418)" role="img" aria-label="Gallery photo of a reception table"></div>
  <div class="abs thumb" style="left:175px;top:2956px;background:linear-gradient(135deg,#4a3a30,#1a1410)" role="img" aria-label="Gallery photo of smoked meat"></div>
  <div class="abs thumb" style="left:304px;top:2956px;background:linear-gradient(135deg,#a04a2a,#4a1a10)" role="img" aria-label="Gallery photo of grilled sausages"></div>
  <div class="abs thumb" style="left:46px;top:3059px;background:linear-gradient(135deg,#c09070,#6a4a38)" role="img" aria-label="Gallery photo of a dining hall"></div>
  <div class="abs thumb" style="left:175px;top:3059px;background:linear-gradient(135deg,#8a4a30,#3a1a10)" role="img" aria-label="Gallery photo of sliced brisket"></div>
  <div class="abs thumb" style="left:304px;top:3059px;background:linear-gradient(135deg,#d0b090,#5a4030)" role="img" aria-label="Gallery photo of a wedding couple"></div>

  <h2 class="abs band-title script" style="left:494px;top:2880px">Testimonial</h2>
  <div class="abs avatar" style="left:496px;top:2950px" role="img" aria-label="Portrait photo of a customer"></div>
  <div class="abs quote-name" style="left:630px;top:2958px">Loren Ipsum</div>
  <div class="abs quote" style="left:630px;top:2990px">It is a long established fact that a reader will be distracted by the readable It is a long established fact that a reader will be</div>
  <svg class="abs" style="left:860px;top:3077px" width="46" height="20" viewBox="0 0 46 20"><circle cx="10" cy="10" r="9" fill="#fff"/><path d="M12 5l-5 5 5 5" stroke="#0d4f9c" stroke-width="2.5" fill="none"/><circle cx="36" cy="10" r="9" fill="#fff"/><path d="M34 5l5 5-5 5" stroke="#0d4f9c" stroke-width="2.5" fill="none"/></svg>

  <!-- flag band & footer -->
  <div class="abs flag-band" role="img" aria-label="Waving American flag banner"></div>
  <footer class="abs footer">
    <h4 style="left:38px">ABOUT US</h4>
    <p class="abs" style="left:38px;top:158px;width:240px">It is a long established fact that a reader will be distracted by the readable content of a page when looking at its layout</p>
    <h4 style="left:332px">SPECIAL LINKS</h4>
    <ul class="abs" style="left:332px;top:158px">
      <li>Home</li><li>About Us</li><li>Our Specialist</li><li>Our Menu</li><li>Contact Us</li>
    </ul>
    <h4 style="left:502px">SUBSCRIBE OUR NEWSLETTER</h4>
    <div class="abs email-field" style="left:502px;top:163px;width:415px;height:41px">enter your e-mail adress</div>
    <div class="abs btn-red" style="left:502px;top:219px;width:103px;height:39px;font-size:11px;font-weight:700">SUBSCRIBE</div>
    <div class="abs copyright" style="left:38px;top:310px">Copyright2017.All Right Reserved</div>
    <div class="abs social" style="left:728px;top:313px"></div>
    <div class="abs social" style="left:768px;top:313px"></div>
    <div class="abs social" style="left:808px;top:313px"></div>
    <div class="abs social" style="left:848px;top:313px"></div>
  </footer>
  <div class="abs brand-mark" style="left:397px;top:3268px;width:184px;height:184px;box-shadow:0 0 0 4px var(--blue)">Hickory<br>Hound<br>BBQ</div>
  <div class="abs footer-line"></div>
</main>
</body>
</html>
```